Harlow Vantor Half Wrap for a Pond Maintenance Bussiness in the UK

Van Wrap Design Brief – Reedmere Basin Ltd
1. Project Overview
We require a half van wrap design for Reedmere Basin Ltd, a professional pond cleaning and maintenance company serving Bedfordshire, Hertfordshire, and Buckinghamshire. The design should communicate reliability, expertise, and our focus on high-quality pond care.
2. Objectives
Make the van instantly recognizable and memorable on the road
Clearly communicate our core services at a glance
Build brand awareness and trust
3. Must-Haves
Company name: “Reedmere Basin Ltd”
Website: https://reedmerebasin.co.uk
Phone number: 01632 960417
Tagline or descriptor: e.g., “Pond Cleaning & Maintenance Specialists”
Imagery or graphics related to ponds, water, or aquatic life
Colour palette: Blues and greens (to suggest water, cleanliness, and nature)
Space for social media icons (Facebook, Instagram, etc.) if possible
Clean, professional fonts
4. Must-Not-Haves
No cartoonish or playful styles
No red or orange colours
Avoid clutter—keep design readable from a distance
No generic stock images or clip-art
5. Style Preferences & Examples
Prefer modern, clean, and bold designs
Like the look of [Competitor A’s van] and [Competitor B’s signage] for their clarity and impact (attach or link examples if possible)
Dislike overly busy or complicated wraps—simplicity and professionalism are key
6. Deliverables & Format
Print-ready files suitable for van wrap production (vector format: AI, EPS, or PDF)
Mockups showing the design on all sides of the van
Colour codes and fonts used
7. Vehicle Details
Harlow Vantor Plus

```html
<!DOCTYPE html>
<html lang="en">
<head>
<meta charset="utf-8">
<title>Reedmere Basin Ltd – Half Wrap Artwork</title>
<link rel="stylesheet" href="https://fonts.googleapis.com/css2?family=Montserrat:wght@300;400;600;700&family=Yellowtail&display=swap">
<style>
  :root {
    --teal: #2cb6cf;
    --blue: #2b45a6;
    --purple: #4a1f8f;
    --green: #7cc242;
    --green-bright: #9bd84a;
    --ink: #222222;
    --logo-grey: #4a4a4a;
    --panel: #ffffff;
    --panel-edge: #d9dce1;
    --bg: #ffffff;
  }
  html, body { margin: 0; padding: 0; overflow: hidden; background: var(--bg); }
  .canvas { width: 1200px; height: 2700px; display: block; }
  .wordmark { font-family: "Montserrat", sans-serif; font-weight: 300; }
  .service { font-family: "Montserrat", sans-serif; font-weight: 700; fill: var(--green-bright); }
  .service-rear { font-family: "Montserrat", sans-serif; font-weight: 700; fill: var(--green-bright); }
  .web { font-family: "Montserrat", sans-serif; font-weight: 400; }
  .phone { font-family: "Montserrat", sans-serif; font-weight: 700; }
  .follow { font-family: "Montserrat", sans-serif; font-weight: 400; }
  .tagline { font-family: "Yellowtail", cursive; fill: var(--ink); }
  .panel-body { fill: var(--panel); stroke: var(--panel-edge); stroke-width: 2; }
  .brand-mark { fill: var(--green); }
</style>
</head>
<body>
<svg class="canvas" viewBox="0 0 1200 2700" xmlns="http://www.w3.org/2000/svg">
  <defs>
    <linearGradient id="wrapGradient" x1="0" y1="0" x2="0" y2="1">
      <stop offset="0" stop-color="var(--teal)"/>
      <stop offset="0.55" stop-color="var(--blue)"/>
      <stop offset="1" stop-color="var(--purple)"/>
    </linearGradient>
    <linearGradient id="markGradient" x1="0" y1="0" x2="1" y2="1">
      <stop offset="0" stop-color="var(--green)"/>
      <stop offset="1" stop-color="var(--blue)"/>
    </linearGradient>
    <clipPath id="sideLeftClip"><rect x="130" y="860" width="880" height="300" rx="30"/></clipPath>
    <clipPath id="rearClip"><rect x="330" y="1360" width="470" height="440" rx="30"/></clipPath>
    <clipPath id="sideRightClip"><rect x="135" y="2150" width="870" height="300" rx="30"/></clipPath>
  </defs>

  <!-- Front bonnet panel -->
  <g class="front-panel">
    <path class="panel-body" d="M300 90 Q575 60 850 90 L860 520 Q575 560 290 520 Z"/>
    <circle cx="482" cy="243" r="3" fill="var(--logo-grey)"/>
    <circle cx="682" cy="243" r="3" fill="var(--logo-grey)"/>
    <circle class="brand-mark" cx="517" cy="263" r="30" fill="url(#markGradient)"/>
    <text class="wordmark" x="560" y="252" font-size="26" fill="var(--logo-grey)">REEDMERE</text>
    <text class="wordmark" x="560" y="287" font-size="26" fill="var(--logo-grey)">BASIN</text>
  </g>

  <!-- Left-hand side panel -->
  <g class="side-panel side-left">
    <rect class="panel-body" x="130" y="860" width="880" height="300" rx="30"/>
    <g clip-path="url(#sideLeftClip)">
      <path d="M790 850 L1020 850 L1020 1170 L360 1170 L360 1145 C560 1105 765 1010 790 850 Z" fill="url(#wrapGradient)"/>
      <path d="M370 1138 C565 1090 752 1000 776 850 L800 850 C782 1012 590 1112 370 1154 Z" fill="var(--green)"/>
    </g>
    <circle class="brand-mark" cx="600" cy="925" r="38" fill="url(#markGradient)"/>
    <text class="wordmark" x="648" y="915" font-size="24" fill="var(--logo-grey)">REEDMERE</text>
    <text class="wordmark" x="648" y="950" font-size="24" fill="var(--logo-grey)">BASIN</text>

    <g class="services">
      <g><circle cx="822" cy="889" r="4.5" fill="var(--green-bright)"/><text class="service" x="832" y="893" font-size="10">POND CLEANING</text></g>
      <g><circle cx="822" cy="906" r="4.5" fill="var(--green-bright)"/><text class="service" x="832" y="910" font-size="10">POND MAINTENANCE</text></g>
      <g><circle cx="822" cy="923" r="4.5" fill="var(--green-bright)"/><text class="service" x="832" y="927" font-size="10">POND BUILDING</text></g>
      <g><circle cx="822" cy="940" r="4.5" fill="var(--green-bright)"/><text class="service" x="832" y="944" font-size="10">POND SERVICES</text></g>
    </g>

    <g class="contact">
      <circle cx="823" cy="1019" r="5" fill="none" stroke="#ffffff" stroke-width="1.5"/>
      <text class="web" x="833" y="1024" font-size="14" fill="#ffffff">reedmerebasin.co.uk</text>
      <path d="M818 1035 q-2 6 4 11 l2 -2 -2 -3 -2 1 q-2 -3 -1 -5 l2 0 0 -3 z" fill="#ffffff"/>
      <text class="phone" x="832" y="1046" font-size="18" fill="var(--green-bright)">01632 960417</text>
      <text class="follow" x="817" y="1066" font-size="12" fill="#ffffff">Follow US:</text>
      <rect x="878" y="1056" width="12" height="12" rx="2" fill="var(--green-bright)"/>
      <rect x="895" y="1056" width="12" height="12" rx="2" fill="var(--green-bright)"/>
      <rect x="912" y="1056" width="12" height="12" rx="2" fill="var(--green-bright)"/>
      <rect x="929" y="1056" width="12" height="12" rx="2" fill="var(--green-bright)"/>
    </g>

    <g transform="rotate(-5 470 1060)">
      <text class="tagline" x="335" y="1052" font-size="28">Pond Cleaning &amp;</text>
      <text class="tagline" x="388" y="1080" font-size="28">Maintenance Specialists</text>
    </g>
  </g>

  <!-- Rear doors panel -->
  <g class="rear-panel">
    <rect class="panel-body" x="330" y="1360" width="470" height="440" rx="30"/>
    <g clip-path="url(#rearClip)">
      <rect x="330" y="1360" width="470" height="440" fill="url(#wrapGradient)"/>
      <path d="M810 1500 C780 1660 570 1745 330 1785 L330 1810 L810 1810 Z" fill="var(--panel)"/>
      <path d="M780 1490 C755 1640 560 1735 360 1770 L362 1782 C575 1752 775 1660 795 1500 Z" fill="var(--green)"/>
      <line x1="572" y1="1360" x2="572" y2="1800" stroke="#1d2a6e" stroke-width="2" opacity="0.5"/>
    </g>
    <circle class="brand-mark" cx="505" cy="1460" r="60" fill="url(#markGradient)"/>
    <text class="wordmark" x="578" y="1445" font-size="34" fill="#ffffff">REEDMERE</text>
    <text class="wordmark" x="578" y="1500" font-size="34" fill="#ffffff">BASIN</text>

    <g class="services">
      <g><circle cx="409" cy="1574" r="5" fill="#cfd6e6"/><text class="service-rear" x="420" y="1578" font-size="12">POND CLEANING</text></g>
      <g><circle cx="409" cy="1595" r="5" fill="#cfd6e6"/><text class="service-rear" x="420" y="1599" font-size="12">POND MAINTENANCE</text></g>
      <g><circle cx="409" cy="1616" r="5" fill="#cfd6e6"/><text class="service-rear" x="420" y="1620" font-size="12">POND BUILDING</text></g>
      <g><circle cx="409" cy="1637" r="5" fill="#cfd6e6"/><text class="service-rear" x="420" y="1641" font-size="12">POND SERVICES</text></g>
    </g>

    <g class="contact">
      <circle cx="620" cy="1719" r="5" fill="none" stroke="var(--purple)" stroke-width="1.5"/>
      <text class="web" x="630" y="1724" font-size="14" fill="var(--purple)">reedmerebasin.co.uk</text>
      <path d="M615 1736 q-2 6 4 11 l2 -2 -2 -3 -2 1 q-2 -3 -1 -5 l2 0 0 -3 z" fill="var(--purple)"/>
      <text class="phone" x="630" y="1749" font-size="19" fill="var(--purple)">01632 960417</text>
      <text class="follow" x="614" y="1770" font-size="12" fill="var(--ink)">Follow US:</text>
      <rect x="678" y="1760" width="12" height="12" rx="2" fill="var(--purple)"/>
      <rect x="696" y="1760" width="12" height="12" rx="2" fill="var(--purple)"/>
      <rect x="714" y="1760" width="12" height="12" rx="2" fill="var(--purple)"/>
      <rect x="732" y="1760" width="12" height="12" rx="2" fill="var(--purple)"/>
    </g>
  </g>

  <!-- Right-hand side panel -->
  <g class="side-panel side-right">
    <rect class="panel-body" x="135" y="2150" width="870" height="300" rx="30"/>
    <g clip-path="url(#sideRightClip)">
      <path d="M125 2140 L350 2140 C372 2300 560 2402 775 2422 L775 2460 L125 2460 Z" fill="url(#wrapGradient)"/>
      <path d="M340 2140 L356 2140 C382 2290 570 2395 775 2412 L775 2430 C560 2412 360 2305 340 2140 Z" fill="var(--green)"/>
    </g>
    <circle class="brand-mark" cx="430" cy="2212" r="38" fill="url(#markGradient)"/>
    <text class="wordmark" x="478" y="2200" font-size="24" fill="var(--logo-grey)">REEDMERE</text>
    <text class="wordmark" x="478" y="2236" font-size="24" fill="var(--logo-grey)">BASIN</text>

    <g class="services">
      <g><circle cx="216" cy="2177" r="4.5" fill="var(--green-bright)"/><text class="service" x="226" y="2181" font-size="10">POND CLEANING</text></g>
      <g><circle cx="216" cy="2194" r="4.5" fill="var(--green-bright)"/><text class="service" x="226" y="2198" font-size="10">POND MAINTENANCE</text></g>
      <g><circle cx="216" cy="2211" r="4.5" fill="var(--green-bright)"/><text class="service" x="226" y="2215" font-size="10">POND BUILDING</text></g>
      <g><circle cx="216" cy="2228" r="4.5" fill="var(--green-bright)"/><text class="service" x="226" y="2232" font-size="10">POND SERVICES</text></g>
    </g>

    <g class="contact">
      <circle cx="211" cy="2290" r="5" fill="none" stroke="var(--green-bright)" stroke-width="1.5"/>
      <text class="web" x="221" y="2295" font-size="14" fill="var(--green-bright)">reedmerebasin.co.uk</text>
      <path d="M206 2306 q-2 6 4 11 l2 -2 -2 -3 -2 1 q-2 -3 -1 -5 l2 0 0 -3 z" fill="#ffffff"/>
      <text class="phone" x="221" y="2318" font-size="18" fill="#ffffff">01632 960417</text>
      <text class="follow" x="205" y="2338" font-size="12" fill="#ffffff">Follow US:</text>
      <rect x="266" y="2328" width="12" height="12" rx="2" fill="var(--green-bright)"/>
      <rect x="283" y="2328" width="12" height="12" rx="2" fill="var(--green-bright)"/>
      <rect x="300" y="2328" width="12" height="12" rx="2" fill="var(--green-bright)"/>
      <rect x="317" y="2328" width="12" height="12" rx="2" fill="var(--green-bright)"/>
    </g>

    <g transform="rotate(5 650 2340)">
      <text class="tagline" x="515" y="2312" font-size="28">Pond Cleaning &amp;</text>
      <text class="tagline" x="565" y="2346" font-size="28">Maintenance Specialists</text>
    </g>
  </g>
</svg>
</body>
</html>
```